website design for a new age Real Estate Security Business

We are launching a business in real estate which no body else is doing. We are going to use technology in terms of software and hardware to provide our services.

We are going to use Big Data, IOT etc.. for our services.

NOTE: We don't want to see Shiel or buildings etc.. that directly suggests Real estate or security on this design

Target Market(s)

India

Industry/Entity Type

Real Estate

Number of Pages Required

4 page

Font styles to use
Sans Serif
Other font styles liked:
• Use Google Fonts

Requirements
Must have
• Home Page should be trendy and colourful should give user confidence to subscribe to our service.
Nice to have
• Use Google fonts.
Should not have
• Design shouldnt have Shield or Buildings that directly suggests real estate or security.

```html
<!DOCTYPE html>
<html lang="en">
<head>
<meta charset="utf-8">
<title>TerraSafe – Data, Analysis, Action</title>
<link rel="stylesheet" href="https://fonts.googleapis.com/css2?family=Bebas+Neue&family=Montserrat:wght@400;500;600;700&family=Playfair+Display:wght@400&display=swap">
<style>
:root{
  --green:#2db75e;
  --green-dark:#3d7a52;
  --blue:#3d8fd9;
  --blue-text:#1f6fc2;
  --ink:#1d1d1d;
  --muted:#555;
  --line:#d8d8d8;
  --navy:#1c2e45;
  --black:#050607;
  --white:#fff;
}
*{box-sizing:border-box;margin:0;padding:0}
html,body{width:1200px;height:3416px;overflow:hidden}
body{font-family:"Montserrat",sans-serif;color:var(--ink);background:var(--white);position:relative}
.abs{position:absolute}

/* Hero */
.hero{position:absolute;left:0;top:0;width:1200px;height:667px;
  background:radial-gradient(ellipse 55% 30% at 60% 42%,#3a3a3a 0%,#161616 45%,var(--black) 80%)}
.hero-rule{position:absolute;left:0;top:74px;width:1200px;height:3px;background:var(--green)}
.nav{position:absolute;top:28px;font-size:17px;font-weight:500;color:var(--white);display:flex;align-items:center;gap:10px}
.brand{position:absolute;left:526px;top:26px;width:148px;height:150px;display:flex;align-items:center;justify-content:center;gap:8px;
  font-size:20px;font-weight:700;color:var(--white);background:var(--black)}
.brand i{display:block;width:12px;height:12px;background:var(--green)}
.hero-title{position:absolute;top:262px;left:0;width:1200px;display:flex;justify-content:center;gap:36px;
  font-family:"Bebas Neue",sans-serif;font-size:50px;color:var(--white);letter-spacing:1px}
.hero-title span{display:flex;align-items:center;gap:8px}
.hero-sub{position:absolute;top:326px;left:0;width:1200px;text-align:center;font-family:"Playfair Display",serif;
  font-size:25px;color:var(--green);letter-spacing:1px}

/* About */
.about{position:absolute;left:87px;top:476px;width:1026px;height:269px;background:var(--white);
  box-shadow:0 4px 14px rgba(0,0,0,.12);text-align:center}
.h2{font-size:34px;font-weight:700;color:var(--ink)}
.h2 em{font-style:normal;color:var(--green)}
.h2 b{color:var(--blue-text)}
.sub{font-size:16px;color:var(--muted)}
.divider{width:262px;height:2px;background:var(--line);margin:0 auto;position:relative}
.divider::after{content:"";position:absolute;left:106px;top:-1px;width:50px;height:4px;background:var(--green)}
.about p.body{font-size:14px;line-height:24px;color:#444;padding:0 58px}

/* Feature sections */
.photo{position:absolute}
.feature h3{font-size:30px;font-weight:400;color:var(--blue-text);letter-spacing:.5px}
.feature p{font-size:14.5px;line-height:24px;color:#333}
.btn-outline{display:inline-flex;align-items:center;gap:6px;border:2px solid #bfe5cc;color:var(--green);
  font-size:13px;font-weight:600;padding:0 14px;height:42px}
.btn-solid{display:inline-flex;align-items:center;gap:6px;background:var(--green);color:var(--white);
  font-size:13px;font-weight:600;padding:0 14px;height:42px}
.land{position:absolute;left:0;top:1355px;width:1200px;height:519px;
  background:linear-gradient(180deg,#b7c8e6 0%,#c9d6ee 55%,#d9e2f2 100%)}

/* Contact */
.contact-photo{position:absolute;left:0;top:2024px;width:597px;height:371px;
  background:linear-gradient(120deg,#c8a98a 0%,#e8d2b6 45%,#b79f87 100%)}
.contact-card{position:absolute;left:87px;top:2077px;width:482px;height:261px;background:rgba(45,45,45,.85);color:var(--white);font-size:14.5px}
.contact-row{position:absolute;left:34px;display:flex;align-items:center;gap:16px;line-height:22px}
.field{position:absolute;left:624px;width:489px;height:47px;border:1px solid #cfcfcf;background:var(--white);
  font-size:12px;color:#9a9a9a;padding:14px 12px}
.send{position:absolute;left:624px;top:2345px;width:489px;height:51px;background:var(--green);color:var(--white);
  display:flex;align-items:center;justify-content:center;gap:8px;font-size:18px;font-weight:600}

/* Pricing */
.plan{position:absolute;top:2584px;width:324px;height:538px;border:2px solid var(--blue);background:var(--white);text-align:center}
.plan-head{height:50px;background:var(--blue);color:var(--white);font-size:23px;font-weight:500;line-height:50px}
.plan-price{height:148px;border-bottom:2px solid var(--blue);display:flex;align-items:center;justify-content:center;gap:8px}
.plan-price strong{font-family:"Bebas Neue",sans-serif;font-weight:400;font-size:72px;color:var(--green);line-height:1}
.plan-price small{font-size:15px;color:var(--green)}
.plan-feats{padding-top:34px;font-size:18px;font-weight:500;color:var(--blue-text);line-height:41px}
.plan-desc{padding:18px 36px 0;font-size:13px;line-height:26px;color:#555}
.plan-more{position:absolute;left:-2px;bottom:-2px;width:324px;height:48px;background:var(--green);color:var(--white);
  font-size:20px;font-weight:600;line-height:48px}

/* Newsletter */
.news-input{position:absolute;left:337px;top:3245px;width:434px;height:42px;border:1px solid #ddd;font-size:11px;color:#999;padding:14px 20px}
.news-btn{position:absolute;left:772px;top:3245px;width:121px;height:42px;background:var(--green-dark);color:var(--white);
  font-size:17px;font-weight:600;text-align:center;line-height:42px}

/* Footer */
.footer{position:absolute;left:0;top:3349px;width:1200px;height:67px;background:var(--navy)}
.footer p{position:absolute;left:87px;top:26px;font-size:12px;color:#7f8ea3}
.social{position:absolute;top:17px;width:34px;height:34px;border:1px solid #6f8099;transform:rotate(45deg)}
</style>
</head>
<body>

<header class="hero" role="img" aria-label="Dark background with a flowing wave of glowing data particles">
  <div class="hero-rule"></div>
  <nav>
    <span class="nav" style="left:152px">Home</span>
    <span class="nav" style="left:253px">About us</span>
    <span class="nav" style="left:380px">Services</span>
    <span class="nav" style="left:751px">Contact</span>
    <span class="nav" style="left:867px">Pricing</span>
    <span class="nav" style="left:966px">
      <svg width="18" height="18" viewBox="0 0 18 18"><circle cx="7.5" cy="7.5" r="5.5" fill="none" stroke="#fff" stroke-width="2.4"/><line x1="11.5" y1="11.5" x2="16" y2="16" stroke="#fff" stroke-width="2.6"/></svg>
    </span>
    <span class="nav" style="left:1026px;gap:6px">
      <svg width="18" height="16" viewBox="0 0 18 16"><path d="M0 1h3l2.5 9h9.5l2-6.5H5" fill="none" stroke="#fff" stroke-width="2"/><circle cx="7" cy="13.5" r="1.6" fill="#fff"/><circle cx="14" cy="13.5" r="1.6" fill="#fff"/></svg>0 Items
    </span>
  </nav>
  <div class="brand"><i></i>TerraSafe</div>
  <h1 class="hero-title">
    <span><svg width="38" height="38" viewBox="0 0 38 38"><path d="M4 19h20M16 10l9 9-9 9" fill="none" stroke="#fff" stroke-width="4"/><path d="M20 4h14v30H20" fill="none" stroke="#fff" stroke-width="0"/></svg>Data</span>
    <span><svg width="38" height="38" viewBox="0 0 38 38"><path d="M4 19h20M16 10l9 9-9 9" fill="none" stroke="#fff" stroke-width="4"/></svg>Analysis</span>
    <span><svg width="38" height="38" viewBox="0 0 38 38"><path d="M4 19h20M16 10l9 9-9 9" fill="none" stroke="#fff" stroke-width="4"/></svg>Action</span>
  </h1>
  <p class="hero-sub">TO KEEP YOUR PROPERTY SAFE</p>
</header>

<section class="about">
  <h2 class="h2" style="margin-top:32px">About <em>TerraSafe</em></h2>
  <p class="sub" style="margin-top:12px">Nemo enim ipsam voluptatem quia voluptas aspernatur</p>
  <div class="divider" style="margin-top:24px"></div>
  <p class="body" style="margin-top:40px">Lorem Ipsum is simply dummy text of the printing and typesetting industry. Lorem Ipsum has been the industry's standard dummy text ever since the 1500s, when an unknown printer took a galley of type and scrambled it to make a type specimen book. It has survived not only five centuries</p>
</section>

<section class="feature">
  <div class="photo" role="img" aria-label="Steel vault door with a yellow document folder in front"
    style="left:87px;top:806px;width:323px;height:446px;background:linear-gradient(135deg,#4a4d52 0%,#2a2c30 55%,#e9cf55 56%,#f3dd78 100%)"></div>
  <div class="abs" style="left:556px;top:862px;width:560px">
    <h3>Doc Secure</h3>
    <p style="margin-top:24px">Lorem Ipsum is simply dummy text of the printing and typesetting industry. Lorem Ipsum has been the industry's standard dummy text ever since the 1500s, when an unknown printer took a galley of type and scrambled it to make a type specimen book. It has survived not only five centuries, but also the leap into electronic typesetting, remaining essentially unchanged. It was popularised in the</p>
    <span class="btn-outline" style="margin-top:46px">LEARN MORE
      <svg width="13" height="13" viewBox="0 0 13 13"><circle cx="6.5" cy="6.5" r="5.5" fill="none" stroke="#2db75e" stroke-width="1.6"/><path d="M4 6.5h4.5M6.5 4.3l2.2 2.2-2.2 2.2" fill="none" stroke="#2db75e" stroke-width="1.5"/></svg></span>
  </div>
</section>

<section class="land feature">
  <div class="photo" role="img" aria-label="Outdoor surveillance camera mounted on a metal pole"
    style="left:626px;top:0;width:574px;height:519px;background:linear-gradient(100deg,rgba(201,214,238,0) 0%,#8b8f97 40%,#3b3d42 60%,#a9afb8 85%,#d0d4da 100%)"></div>
  <div class="abs" style="left:87px;top:99px;width:520px">
    <h3>Land Secure</h3>
    <p style="margin-top:24px">Lorem Ipsum is simply dummy text of the printing and typesetting industry. Lorem Ipsum has been the industry's standard dummy text ever since the 1500s, when an unknown printer took a galley of type and scrambled it to make a type specimen book. It has survived not only five centuries, but also the leap into electronic typesetting, remaining essentially unchanged. It was popularised in the</p>
    <span class="btn-solid" style="margin-top:44px">LEARN MORE
      <svg width="13" height="13" viewBox="0 0 13 13"><circle cx="6.5" cy="6.5" r="5.5" fill="none" stroke="#fff" stroke-width="1.6"/><path d="M4 6.5h4.5M6.5 4.3l2.2 2.2-2.2 2.2" fill="none" stroke="#fff" stroke-width="1.5"/></svg></span>
  </div>
</section>

<section class="contact">
  <h2 class="h2 abs" style="left:0;top:1926px;width:1200px;text-align:center;font-size:31px">Get in <b>touch</b></h2>
  <div class="divider abs" style="left:469px;top:1984px;margin:0"></div>
  <div class="contact-photo" role="img" aria-label="Blurred photo of hands working at a desk"></div>
  <div class="contact-card">
    <div class="contact-row" style="top:52px">
      <svg width="20" height="24" viewBox="0 0 20 24"><path d="M10 1a8 8 0 0 0-8 8c0 6 8 14 8 14s8-8 8-14a8 8 0 0 0-8-8z" fill="#2db75e"/><circle cx="10" cy="9" r="3" fill="#2d2d2d"/></svg>
      <span>Lorem Ipsum is that it has a more-or-less<br>normal distribution of letters</span></div>
    <div class="contact-row" style="top:121px">
      <svg width="20" height="20" viewBox="0 0 20 20"><path d="M4 1l4 4-2.5 3a12 12 0 0 0 6.5 6.5l3-2.5 4 4-3 3C8 18 2 12 1 4z" fill="#2db75e"/></svg>
      <span>Phone Number: +1-555-014-2290</span></div>
    <div class="contact-row" style="top:188px">
      <svg width="20" height="18" viewBox="0 0 20 18"><rect x="1" y="3" width="18" height="14" fill="#2db75e"/><path d="M1 3l9 7 9-7" fill="none" stroke="#2d2d2d" stroke-width="1.6"/></svg>
      <span>Email: info@terrasafe-mail.com</span></div>
  </div>
  <div class="field" style="top:2024px">Your name</div>
  <div class="field" style="top:2090px">Your email</div>
  <div class="field" style="top:2155px">Subject</div>
  <div class="field" style="top:2220px;height:102px">Your message</div>
  <div class="send">
    <svg width="20" height="18" viewBox="0 0 20 18"><path d="M1 8l18-7-4 16-5-5-3 5V11l10-9-12 8z" fill="#fff"/></svg>Send Message</div>
</section>

<section class="pricing">
  <h2 class="h2 abs" style="left:0;top:2448px;width:1200px;text-align:center;font-size:31px">Our <b>Pricing</b></h2>
  <p class="sub abs" style="left:0;top:2497px;width:1200px;text-align:center;font-size:15px">Nemo enim ipsam voluptatem quia voluptas aspernatur</p>
  <div class="divider abs" style="left:469px;top:2545px;margin:0"></div>

  <article class="plan" style="left:87px">
    <div class="plan-head">Standard</div>
    <div class="plan-price"><strong>$1,99</strong><small>Per/Month</small></div>
    <div class="plan-feats">10 GB<br>1 Domain<br>4 mail</div>
    <p class="plan-desc">type specimen book. It has survived not only five centuries, but also the leap into electronic typesetting</p>
    <div class="plan-more">More</div>
  </article>
  <article class="plan" style="left:438px">
    <div class="plan-head">Extended</div>
    <div class="plan-price"><strong>$1,99</strong><small>Per/Month</small></div>
    <div class="plan-feats">10 GB<br>1 Domain<br>4 mail</div>
    <p class="plan-desc">type specimen book. It has survived not only five centuries, but also the leap into electronic typesetting</p>
    <div class="plan-more">More</div>
  </article>
  <article class="plan" style="left:789px">
    <div class="plan-head">Premium</div>
    <div class="plan-price"><strong>$1,99</strong><small>Per/Month</small></div>
    <div class="plan-feats">10 GB<br>1 Domain<br>4 mail</div>
    <p class="plan-desc">type specimen book. It has survived not only five centuries, but also the leap into electronic typesetting</p>
    <div class="plan-more">More</div>
  </article>
</section>

<section class="newsletter">
  <h2 class="h2 abs" style="left:0;top:3178px;width:1200px;text-align:center;font-size:31px">Subscribe to the <b>NewsLetter</b></h2>
  <div class="news-input">Your Email Here</div>
  <div class="news-btn">Subscribe</div>
</section>

<footer class="footer">
  <p>2017 © TerraSafe. All Rights Reserved</p>
  <span class="social" style="left:909px"></span>
  <span class="social" style="left:965px"></span>
  <span class="social" style="left:1020px"></span>
  <span class="social" style="left:1075px"></span>
</footer>

</body>
</html>
```